Request for Business Card Design

Hi. My name is Marlena, I am looking for a new business card design for my company, Quillbrook Sensing Systems, LLC. I really like the design you did for Tavel Harvest and was hoping you could do something similar using our full logo and our mark. I am also open to any raised texture design using our mark. I have attached our full logo, which would need to be somewhere on the card, as well as the mark in both outline and full form, as well as our brand colors / guide. The card does not have to be white, as long as our logo and mark appear. I actually like darker colored business cards more, but am open to all options. If you are interested in working with me, please let me know. We would also take the business card design into letterhead design if you can do that.

```html
<!DOCTYPE html>
<html lang="en">
<head>
<meta charset="utf-8">
<title>Quillbrook Sensing Systems — Business Card</title>
<link rel="stylesheet" href="https://fonts.googleapis.com/css2?family=Montserrat:wght@300;400;700&display=swap">
<style>
  :root {
    --brand-blue: #1a9bc2;
    --brand-tint: #e4f2f8;
    --ink: #3b3b3d;
    --paper: #ffffff;
    --backdrop: #eceef1;
  }
  * { margin: 0; padding: 0; box-sizing: border-box; }
  html, body {
    width: 1198px; height: 1200px; overflow: hidden;
    background: var(--backdrop);
    font-family: "Montserrat", sans-serif;
  }
  .card {
    position: absolute; left: 167px;
    width: 864px; height: 510px;
    background: var(--paper);
    overflow: hidden;
  }
  .card--front { top: 74px; }
  .card--back { top: 621px; }
  .card__art { position: absolute; inset: 0; width: 100%; height: 100%; }

  .company-name {
    position: absolute; left: 60px; top: 70px;
    color: var(--brand-blue);
    font-weight: 700; font-size: 23px; line-height: 34px;
    letter-spacing: 0.5px; text-transform: uppercase;
  }
  .brand-lockup {
    position: absolute; display: flex; align-items: center; gap: 14px;
  }
  .card--front .brand-lockup { left: 60px; top: 260px; }
  .card--back .brand-lockup { left: 90px; top: 326px; }
  .brand-lockup__dot {
    width: 54px; height: 54px; border-radius: 50%;
    background: var(--brand-blue);
  }
  .brand-lockup__name {
    color: var(--ink); font-weight: 700; font-size: 36px;
    letter-spacing: 2px;
  }

  .holder-name {
    position: absolute; right: 60px; top: 152px;
    color: var(--paper); font-weight: 700; font-size: 27px;
    letter-spacing: 1px; text-transform: uppercase;
  }
  .contact-list {
    position: absolute; right: 58px; top: 216px;
    list-style: none; color: var(--paper);
    font-weight: 300; font-size: 20px;
  }
  .contact-list li {
    display: flex; justify-content: flex-end; align-items: center;
    gap: 14px; height: 33px;
  }
  .contact-list .contact-list__address {
    margin-top: 44px; height: auto; align-items: flex-start; text-align: right;
    line-height: 29px;
  }
  .contact-icon { width: 16px; height: 16px; flex: none; fill: var(--paper); }
  .contact-list__address .contact-icon { margin-top: 6px; }
</style>
</head>
<body>

<section class="card card--front" aria-label="Business card front">
  <svg class="card__art" viewBox="0 0 864 510" aria-hidden="true">
    <path fill="var(--brand-blue)" d="M454 0 H864 V510 H196 C390 470 515 350 508 225 C503 140 485 60 454 0 Z"/>
    <path fill="none" stroke="var(--brand-blue)" stroke-width="7" d="M430 0 C462 60 483 140 488 225 C495 345 370 465 163 510"/>
  </svg>

  <h1 class="company-name">Quillbrook Sensing<br>Systems, LLC</h1>

  <div class="brand-lockup">
    <span class="brand-lockup__dot"></span>
    <span class="brand-lockup__name">QUILLBROOK</span>
  </div>

  <h2 class="holder-name">Marlena</h2>

  <ul class="contact-list">
    <li>508-472-3190
      <svg class="contact-icon" viewBox="0 0 16 16"><path d="M3 1l3 3-1.5 2a9 9 0 0 0 5.5 5.5L12 10l3 3-2 2C7 15 1 9 1 3z"/></svg>
    </li>
    <li>508-472-3191
      <svg class="contact-icon" viewBox="0 0 16 16"><path d="M4 1h8v4H4zM1 6h14v6h-3v3H4v-3H1zm4 4v3h6v-3z"/></svg>
    </li>
    <li>hello@quillbrook.com
      <svg class="contact-icon" viewBox="0 0 16 16"><path d="M1 3h14v10H1zm1.5 1.5L8 9l5.5-4.5z"/></svg>
    </li>
    <li>www.quillbrook.com
      <svg class="contact-icon" viewBox="0 0 16 16"><path d="M8 1a7 7 0 1 0 0 14A7 7 0 0 0 8 1zm0 1.5c1 1.2 1.6 2.8 1.7 4.7H6.3C6.4 5.3 7 3.7 8 2.5zM2.6 8.8h2.2c.1 1.7.6 3.2 1.3 4.3a5.5 5.5 0 0 1-3.5-4.3zm0-1.6a5.5 5.5 0 0 1 3.5-4.3c-.7 1.1-1.2 2.6-1.3 4.3zm3.7 1.6h3.4c-.1 1.8-.7 3.4-1.7 4.7-1-1.3-1.6-2.9-1.7-4.7zm4.9 0h2.2a5.5 5.5 0 0 1-3.5 4.3c.7-1.1 1.2-2.6 1.3-4.3zm0-1.6c-.1-1.7-.6-3.2-1.3-4.3a5.5 5.5 0 0 1 3.5 4.3z"/></svg>
    </li>
    <li class="contact-list__address">27 Arden Way, Suite 210<br>Lowell MA 01852
      <svg class="contact-icon" viewBox="0 0 16 16"><path d="M8 0a5 5 0 0 0-5 5c0 3.5 5 8 5 8s5-4.5 5-8a5 5 0 0 0-5-5zm0 3a2 2 0 1 1 0 4 2 2 0 0 1 0-4zM2 14h12v2H2z"/></svg>
    </li>
  </ul>
</section>

<section class="card card--back" aria-label="Business card back">
  <svg class="card__art" viewBox="0 0 864 510" aria-hidden="true">
    <circle cx="560" cy="250" r="300" fill="var(--brand-tint)"/>
  </svg>
  <div class="brand-lockup">
    <span class="brand-lockup__dot"></span>
    <span class="brand-lockup__name">QUILLBROOK</span>
  </div>
</section>

</body>
</html>
```